Custom PowerPoint Template for Training & Workshop Presentations

I am looking for a professional designer to create a custom PowerPoint template (PPTX) for my training and workshop materials. My trainings are designed for: HR professionals and Learning & Development specialists;
Executives and team leaders; Organizations investing in employee development and workplace learning; Participants in professional development workshops, seminars, and didactics trainings
The template should therefore appear trustworthy, calm, friendly, structured, and competence‑oriented. The design should be visually appealing, easy to read, and fully editable.

All branding files are attached to this project.
Please use them as the main reference for your design:
Logo (included as attachment)
Brand color specifications (included as attachment)
Font specifications related to the logo and brand (included as attachment)

What I need:
--> Title Slide: Title, subtitle, name, logo
(1–2 variations)
--> Agenda / Overview Slide
--> Content Slides
--> Text only
--> Text + image
-->Two-column
--> Section header
--> Quote / key message
--> Graphic / Model Slides: (1–2 layouts for frameworks, processes, models)
--> Tables & Charts: (Table styles in brand colors; Chart design aligned with typography and color palette)
--> Closing Slide: (Contact or call-to-action; Optional second variation)

All layouts must be built properly inside the PowerPoint Slide Master

```html
<!DOCTYPE html>
<html lang="de">
<head>
<meta charset="utf-8">
<title>Präsentationsvorlage – Trainings &amp; Workshops</title>
<link href="https://fonts.googleapis.com/css2?family=Roboto:wght@400;500;700&display=swap" rel="stylesheet">
<style>
  :root {
    --stage: #474f57;
    --brand: #175e93;
    --brand-soft: #8daac2;
    --brand-muted: #7d9ab5;
    --paper: #ffffff;
    --ink: #3a3f45;
    --placeholder: #e4e6e8;
  }
  * { margin: 0; padding: 0; box-sizing: border-box; }
  html, body { width: 1200px; height: 1001px; overflow: hidden; }
  body { background: var(--stage); font-family: "Roboto", Arial, sans-serif; position: relative; color: var(--ink); }
  .slide { position: absolute; width: 362px; height: 204px; background: var(--paper); overflow: hidden; }
  .slide > * { position: absolute; }
  .col-1 { left: 39px; } .col-2 { left: 417px; } .col-3 { left: 798px; }
  .row-1 { top: 180px; } .row-2 { top: 398px; } .row-3 { top: 617px; }
  .slide--solid { background: var(--brand); }

  .kicker { font-size: 7.2px; font-weight: 500; line-height: 9px; color: var(--brand-muted); letter-spacing: .1px; }
  .kicker strong { display: block; color: var(--brand); font-weight: 700; }
  .kicker::after { content: ""; display: block; width: 14px; height: 1.5px; background: var(--brand); margin-top: 3px; }
  .heading { font-size: 7.6px; font-weight: 700; color: var(--brand); }
  .body { font-size: 4.2px; line-height: 6.6px; color: var(--ink); }
  .placeholder { background: var(--placeholder); }

  /* title slide */
  .brand-name { left: 34px; top: 38px; display: flex; align-items: center; gap: 4px; font-size: 6.4px; font-weight: 700; color: var(--brand); }
  .brand-name i { width: 12px; height: 12px; border: 1px solid var(--brand-soft); display: block; }
  .title { left: 34px; top: 72px; font-size: 15px; line-height: 16.5px; font-weight: 700; color: var(--brand); }
  .subtitle { left: 34px; top: 146px; font-size: 5.6px; color: var(--brand-soft); }
  .web { left: 34px; top: 170px; display: flex; align-items: center; gap: 4px; font-size: 5.6px; color: var(--brand-soft); }
  .web i { width: 11px; height: 11px; border-radius: 50%; background: var(--brand); display: block; }
  .hero-shape { left: 201px; top: 30px; width: 144px; height: 144px; background: var(--brand); border-radius: 6px; }

  /* numbered */
  .num { width: 24px; height: 24px; color: #fff; font-size: 8px; display: flex; align-items: center; justify-content: center; }
  .num--dark { background: var(--brand); } .num--soft { background: var(--brand-soft); }
  .icon-dot { width: 22px; height: 22px; border-radius: 50%; display: flex; align-items: center; justify-content: center; }
  .centered { text-align: center; }

  /* model slide */
  .model-title { font-size: 6.4px; font-weight: 400; color: var(--ink); }
  .model-left { text-align: right; }
  .model-graphic { left: 116px; top: 63px; width: 129px; height: 104px; background: linear-gradient(135deg, var(--brand), var(--brand-soft)); }

  .closing-panel { left: 0; top: 0; width: 159px; height: 204px; background: var(--brand); }
  .thanks { left: 18px; top: 91px; font-size: 14px; font-weight: 700; color: #fff; }
  .contact { left: 18px; top: 118px; font-size: 3.4px; line-height: 5px; color: #fff; }
</style>
</head>
<body>

<section class="slide col-1 row-1">
  <div class="brand-name"><i></i>Dr. Lena Hartwig-Bauer</div>
  <h1 class="title">Trainings,<br>Workshops,<br>Beratung<br>und Coachings</h1>
  <p class="subtitle">Hol dir Impulse zu Lehren &amp; Resilienz</p>
  <p class="web"><i></i>www.lenahartwig.de</p>
  <div class="hero-shape" role="img" aria-label="Große Markengrafik in Blau"></div>
</section>

<section class="slide col-2 row-1">
  <p class="kicker" style="left:23px;top:18px">GEMEINSAM KOMPETENZEN<strong>ENTWICKELN</strong></p>
  <h2 class="heading" style="left:23px;top:82px">SLIDE PRESENTATION</h2>
  <p class="body" style="left:23px;top:96px;width:155px">Lorem ipsum dolor sit amet, consectetur adipiscing elit, sed do eiusmod tempor incididunt ut labore et dolore magna aliqua. Ut enim ad minim veniam. Lorem ipsum dolor sit amet, consectetur adipiscing elit, sed do eiusmod tempor incididunt ut labore et dolore magna aliqua. Ut enim ad minim veniam.</p>
  <div class="placeholder" style="left:207px;top:30px;width:144px;height:144px" role="img" aria-label="Bildplatzhalter"></div>
  <div style="left:161px;top:144px;width:62px;height:18px;background:var(--brand-soft)"></div>
</section>

<section class="slide slide--solid col-3 row-1"></section>

<section class="slide col-1 row-2">
  <p class="kicker" style="left:22px;top:22px">GEMEINSAM KOMPETENZEN<strong>ENTWICKELN</strong></p>
  <p class="body" style="left:22px;top:63px;width:132px">Lorem ipsum dolor sit amet, consectetur adipiscing elit, sed do eiusmod tempor incididunt ut labore et dolore magna aliqua. Ut enim ad minim veniam. Lorem ipsum dolor sit amet, consectetur adipiscing elit.</p>
  <p class="body" style="left:208px;top:63px;width:132px">Lorem ipsum dolor sit amet, consectetur adipiscing elit, sed do eiusmod tempor incididunt ut labore et dolore magna aliqua. Ut enim ad minim veniam. Lorem ipsum dolor sit amet, consectetur adipiscing elit.</p>
  <div class="placeholder" style="left:0;top:110px;width:111px;height:76px" role="img" aria-label="Bildplatzhalter"></div>
  <div style="left:111px;top:110px;width:140px;height:76px;background:var(--brand)"></div>
  <div style="left:251px;top:110px;width:111px;height:76px;background:var(--brand-soft)"></div>
</section>

<section class="slide col-2 row-2">
  <p class="kicker" style="left:21px;top:14px">GEMEINSAM KOMPETENZEN<strong>ENTWICKELN</strong></p>
  <div class="num num--dark" style="left:22px;top:60px">01</div>
  <p class="body" style="left:54px;top:62px;width:112px">Lorem ipsum dolor sit amet, consectetur adipiscing elit, sed do eiusmod tempor incididunt ut labore et dolore magna aliqua.</p>
  <div class="num num--soft" style="left:198px;top:60px">02</div>
  <p class="body" style="left:231px;top:62px;width:112px">Lorem ipsum dolor sit amet, consectetur adipiscing elit, sed do eiusmod tempor incididunt ut labore et dolore magna aliqua.</p>
  <div class="num num--soft" style="left:22px;top:94px">03</div>
  <p class="body" style="left:54px;top:96px;width:112px">Lorem ipsum dolor sit amet, consectetur adipiscing elit, sed do eiusmod tempor incididunt ut labore et dolore magna aliqua.</p>
  <div class="num num--dark" style="left:198px;top:94px">04</div>
  <p class="body" style="left:231px;top:96px;width:112px">Lorem ipsum dolor sit amet, consectetur adipiscing elit, sed do eiusmod tempor incididunt ut labore et dolore magna aliqua.</p>
  <h2 class="heading centered" style="left:0;width:362px;top:144px">SLIDE PRESENTATION</h2>
  <p class="body centered" style="left:25px;width:312px;top:158px">Lorem ipsum dolor sit amet, consectetur adipiscing elit, sed do eiusmod tempor incididunt ut labore et dolore magna aliqua. Ut enim ad minim veniam. Lorem ipsum dolor sit amet, consectetur adipiscing elit, sed do eiusmod tempor incididunt ut labore et dolore magna aliqua.</p>
</section>

<section class="slide col-3 row-2">
  <p class="kicker" style="left:26px;top:14px">GEMEINSAM KOMPETENZEN<strong>ENTWICKELN</strong></p>
  <h2 class="heading" style="left:26px;top:73px">SLIDE PRESENTATION</h2>
  <p class="body" style="left:26px;top:86px;width:180px">Lorem ipsum dolor sit amet, consectetur adipiscing elit, sed do eiusmod tempor incididunt ut labore et dolore magna aliqua. Ut enim ad minim veniam.</p>
  <div class="icon-dot" style="left:226px;top:54px;background:var(--brand-soft)">
    <svg width="10" height="10" viewBox="0 0 10 10" fill="none" stroke="#fff" stroke-width="1"><rect x="2.5" y="1" width="5" height="3"/><rect x="1" y="4" width="8" height="3.5"/><rect x="3" y="6" width="4" height="3"/></svg>
  </div>
  <p class="body" style="left:251px;top:58px;width:100px">Lorem ipsum dolor sit amet, consectetur adipiscing elit.</p>
  <div class="icon-dot" style="left:226px;top:85px;background:var(--brand)">
    <svg width="10" height="10" viewBox="0 0 10 10" fill="none" stroke="#fff" stroke-width="1"><path d="M3 1.5h4v7L5 7 3 8.5z"/></svg>
  </div>
  <p class="body" style="left:251px;top:89px;width:100px">Lorem ipsum dolor sit amet, consectetur adipiscing elit.</p>
  <div class="placeholder" style="left:0;top:112px;width:362px;height:92px" role="img" aria-label="Bildplatzhalter"></div>
</section>

<section class="slide col-1 row-3">
  <p class="kicker" style="left:22px;top:18px">GEMEINSAM KOMPETENZEN<strong>ENTWICKELN</strong></p>
  <div class="placeholder" style="left:23px;top:75px;width:182px;height:103px" role="img" aria-label="Bildplatzhalter"></div>
  <h2 class="heading" style="left:214px;top:108px">SLIDE PRESENTATION</h2>
  <p class="body" style="left:214px;top:124px;width:130px">Lorem ipsum dolor sit amet, consectetur adipiscing elit, sed do eiusmod tempor incididunt ut labore et dolore magna aliqua. Ut enim ad minim veniam. Lorem ipsum dolor sit amet, consectetur adipiscing elit, sed do eiusmod tempor incididunt ut labore et dolore magna aliqua. Ut enim ad minim veniam.</p>
</section>

<section class="slide col-2 row-3">
  <p class="kicker" style="left:26px;top:18px">GEMEINSAM KOMPETENZEN<strong>ENTWICKELN</strong></p>
  <div class="model-graphic" role="img" aria-label="Modellgrafik mit vier Bausteinen"></div>
  <p class="model-title model-left" style="left:0;width:111px;top:58px">YOUR TITLE</p>
  <p class="body model-left" style="left:36px;width:75px;top:70px">Lorem ipsum dolor sit amet, consectetur adipiscing elit, sed do eiusmod tempor incididunt.</p>
  <p class="model-title model-left" style="left:0;width:111px;top:136px">YOUR TITLE</p>
  <p class="body model-left" style="left:36px;width:75px;top:148px">Lorem ipsum dolor sit amet, consectetur adipiscing elit, sed do eiusmod tempor incididunt.</p>
  <p class="model-title" style="left:251px;top:58px">YOUR TITLE</p>
  <p class="body" style="left:251px;width:78px;top:70px">Lorem ipsum dolor sit amet, consectetur adipiscing elit, sed do eiusmod tempor incididunt.</p>
  <p class="model-title" style="left:251px;top:136px">YOUR TITLE</p>
  <p class="body" style="left:251px;width:78px;top:148px">Lorem ipsum dolor sit amet, consectetur adipiscing elit, sed do eiusmod tempor incididunt.</p>
</section>

<section class="slide col-3 row-3">
  <div class="closing-panel"></div>
  <h2 class="thanks">Thank you</h2>
  <p class="contact">Dr. phil. Lena Hartwig-Bauer, MBA<br>Expertin für Didaktik und Selbstführung<br><br>Kontakt<br><br>Dr. phil. Lena Hartwig-Bauer, MBA<br>Lindenweg 12<br>90402 Nürnberg<br><br>E-Mail: info@lenahartwig.de<br>Telefon: 0170 / 1234567</p>
</section>

</body>
</html>
```